Newlyweds banner image for wedding reception

Banner with the words “The Newlyweds” (No quotations) in an elegant and thick (bold) font. Font must be easy to read. Gold or silver letters. Words should easily be edited so that we have the option to print in gold or silver. No background. Image must have source file as well as be delivered as a png with a transparent background. Image will be printed in a horizontal orientation. Must be 300 Dpi for printing. Image must not lose any quality and remain crisp and sharp when expanded and printed to a size of up to 6 feet wide and 2 feet tall. Be creative but we are looking for an elegant option. First and foremost.

Target Market(s)

Wedding planners, brides planning wedding and reception

Industry/Entity Type

Wedding decoration

Colors

Designer to choose colors to be used in the design.

Requirements
Must have
• Gold or Silver letters
Should not have
• Do not mix colors

```html
<!DOCTYPE html>
<html lang="en">
<head>
<meta charset="UTF-8">
<title>The Newlyweds – Reception Banner</title>
<link rel="stylesheet" href="https://fonts.googleapis.com/css2?family=Montserrat:wght@900&display=swap">
<style>
  :root {
    --page-bg: #eeeeec;
    --banner-bg: #ffffff;
    --gold-light: #f0c85a;
    --gold-mid: #d9a62e;
    --gold-deep: #b8861c;
    --frame-gold: #d6a53a;
    --flourish-light: #f7e6b8;
    --flourish-deep: #ecd08a;
  }
  html, body {
    margin: 0;
    padding: 0;
    width: 1200px;
    height: 709px;
    overflow: hidden;
    background: var(--page-bg);
  }
  .canvas {
    position: relative;
    width: 1200px;
    height: 709px;
  }
  .banner {
    position: absolute;
    left: 40px;
    top: 164px;
    width: 1120px;
    height: 380px;
    background: var(--banner-bg);
    box-shadow: 0 2px 10px rgba(0, 0, 0, 0.08);
    overflow: hidden;
  }
  .banner-frame {
    position: absolute;
    inset: 14px;
    border: 3px solid var(--frame-gold);
  }
  .flourish {
    position: absolute;
    border-radius: 40px;
    background: linear-gradient(90deg, var(--flourish-light) 0%, var(--flourish-deep) 50%, var(--flourish-light) 100%);
  }
  .flourish--left {
    left: 90px;
    top: 46px;
    width: 390px;
    height: 84px;
  }
  .flourish--right {
    left: 740px;
    top: 112px;
    width: 290px;
    height: 70px;
  }
  .title {
    position: absolute;
    left: 0;
    right: 0;
    margin: 0;
    text-align: center;
    font-family: 'Montserrat', sans-serif;
    font-weight: 900;
    line-height: 1;
    text-transform: uppercase;
    white-space: nowrap;
    color: var(--gold-mid);
    background: linear-gradient(180deg, var(--gold-light) 0%, var(--gold-mid) 55%, var(--gold-deep) 100%);
    -webkit-background-clip: text;
    background-clip: text;
    -webkit-text-fill-color: transparent;
  }
  .title--small {
    top: 96px;
    padding-left: 90px;
    font-size: 72px;
    letter-spacing: 3px;
  }
  .title--large {
    top: 196px;
    font-size: 126px;
    letter-spacing: 4px;
  }
</style>
</head>
<body>
<div class="canvas">
  <div class="banner">
    <div class="banner-frame"></div>
    <div class="flourish flourish--left" role="img" aria-label="Gold decorative swirl flourish"></div>
    <div class="flourish flourish--right" role="img" aria-label="Gold decorative swirl flourish"></div>
    <h1 class="title title--small">The</h1>
    <p class="title title--large">Newlyweds</p>
  </div>
</div>
</body>
</html>
```